Cover of the e-book award-winning national sports figure.

I would like to utilize the picture this attached to this brief. If you could pull the trophies and myself out and place with the new background, that’s what I would like to see . I would like to have a new bookcover design for my e-book. I attached below the original cover and have marked in red. The things that I don’t want on the new cover. I’ve attached a picture that’s not the original. I’m waiting on the high copy. I would like to replace the old logo with the one that I have attached. The website that I would like to have on the book is www.dellanvmoreaux.com.
Target Market(s)
Biography
Industry/Entity Type
Sports & motivation?
Requirements
Must have
- Picture of me in the blue suit on the cover the title of the book walking past midnight lessons from quiet harbors
Nice to have
- Utilize the old cover that I have attached for some ideas
Should not have
- The cover should not have anything related to marlow crest press Inc.

```html
<!DOCTYPE html>
<html lang="en">
<head>
<meta charset="utf-8">
<title>Walking Past Midnight — Jacket Spread</title>
<link href="https://fonts.googleapis.com/css2?family=Oswald:wght@500;700&family=Poppins:wght@700;800&family=Montserrat:wght@400;500;600;700&display=swap" rel="stylesheet">
<style>
  :root {
    --navy: #0b2a66;
    --navy-deep: #08214f;
    --sky: #2b8fe8;
    --white: #ffffff;
    --ink: #1d1d1f;
    --stage: #e6e7e9;
  }
  * { margin: 0; padding: 0; box-sizing: border-box; }
  html, body { width: 1200px; height: 2498px; overflow: hidden; }
  body { background: var(--stage); font-family: "Montserrat", sans-serif; position: relative; }

  .jacket {
    position: absolute; left: 70px; top: 1019px; width: 1060px; height: 460px;
    background: var(--white); box-shadow: 0 10px 30px rgba(0,0,0,.18);
  }
  .flap { position: absolute; top: 0; height: 460px; padding: 22px 18px; color: var(--ink); }
  .flap p { font-size: 5.2px; line-height: 1.45; text-align: justify; margin-bottom: 6px; }
  .flap--back { left: 0; width: 194px; }
  .flap--front { left: 857px; width: 203px; }
  .flap-note { font-size: 5px; margin-bottom: 8px; }
  .flap-title { font-family: "Oswald", sans-serif; font-weight: 500; color: var(--sky); font-size: 12px; line-height: 1; }
  .flap-subtitle { font-weight: 700; font-size: 8px; margin: 3px 0 6px; }
  .flap-sign { position: absolute; left: 30px; bottom: 18px; text-align: center; }
  .brand { display: flex; align-items: center; gap: 4px; font-weight: 600; color: var(--navy); font-size: 7px; }
  .brand-dot { width: 14px; height: 14px; border-radius: 50%; background: var(--sky); flex: none; }
  .flap-url { font-size: 6px; margin-top: 4px; color: var(--ink); }

  .panel { position: absolute; top: 0; height: 390px; background: var(--navy); }
  .panel--back { left: 194px; width: 316px; background: var(--navy-deep); }
  .panel--spine { left: 510px; width: 67px; background: var(--navy-deep); }
  .panel--front { left: 577px; width: 280px; background: linear-gradient(180deg, #0c3478 0%, var(--navy) 100%); }

  .back-photo { position: absolute; left: 33px; top: 25px; width: 237px; height: 150px; border: 2px solid var(--sky); border-radius: 8px; background: linear-gradient(180deg, #e8eaee, #b9433f 75%, #6a8a4a); }
  .back-heading { position: absolute; left: 20px; top: 186px; width: 276px; text-align: center; color: var(--white); font-weight: 600; font-size: 11px; line-height: 1.15; }
  .back-body { position: absolute; left: 24px; top: 218px; width: 268px; text-align: center; color: var(--white); font-size: 6.3px; line-height: 1.5; }
  .back-brand { position: absolute; left: 26px; top: 330px; color: var(--white); }
  .back-brand .brand { color: var(--white); font-size: 6px; }
  .back-url { font-size: 6px; margin-top: 6px; }
  .back-charity { position: absolute; left: 132px; top: 340px; width: 140px; font-size: 5.5px; font-style: italic; color: #b9c7e0; }

  .spine-text { position: absolute; writing-mode: vertical-rl; display: flex; align-items: center; font-family: "Oswald", sans-serif; font-weight: 500; color: var(--white); }
  .spine-author { top: 22px; left: 6px; width: 30px; font-size: 13px; letter-spacing: .5px; }
  .spine-title { top: 110px; left: 6px; width: 30px; font-size: 15px; }
  .spine-title em { font-style: normal; color: var(--sky); }
  .spine-foreword { top: 300px; left: 2px; width: 48px; font-size: 10px; line-height: 1.05; }

  .title-bar { position: absolute; background: var(--sky); }
  .title-bar--stem { left: 5px; top: 0; width: 15px; height: 235px; }
  .title-bar--foot { left: 5px; top: 220px; width: 40px; height: 15px; }
  .title { position: absolute; left: 28px; font-family: "Oswald", sans-serif; font-weight: 700; line-height: .9; white-space: nowrap; }
  .title--lead { top: 30px; font-size: 58px; color: #e9ebef; letter-spacing: -1px; }
  .title--mid { top: 92px; font-size: 40px; color: var(--sky); font-family: "Poppins", sans-serif; font-weight: 800; }
  .title--tail { top: 142px; font-size: 52px; color: #e9ebef; letter-spacing: -1px; }
  .subtitle { position: absolute; left: 24px; top: 246px; font-family: "Poppins", sans-serif; font-weight: 800; color: var(--white); font-size: 17px; line-height: 1.05; }
  .author { position: absolute; left: 24px; top: 302px; font-family: "Oswald", sans-serif; font-weight: 700; color: var(--white); font-size: 30px; line-height: 1; }
  .trophies { position: absolute; left: 150px; top: 305px; width: 48px; height: 85px; background: linear-gradient(180deg, #c7ccd4, #6b5a47); border-radius: 6px 6px 2px 2px; }
  .portrait { position: absolute; left: 190px; top: 218px; width: 90px; height: 242px; background: linear-gradient(180deg, #3a2a22 0%, #1f3f86 22%, #17346f 100%); border-radius: 40px 40px 0 0; }
  .foreword { position: absolute; left: 598px; top: 404px; }
  .foreword-label { font-size: 9px; font-weight: 600; color: var(--navy); }
  .foreword-name { font-size: 16px; font-weight: 700; color: var(--ink); letter-spacing: .3px; white-space: nowrap; }
</style>
</head>
<body>
<main class="jacket">
  <section class="flap flap--back">
    <p class="flap-note">(Continued from front flap)</p>
    <p>which meant he had to earn every snap from the bottom of the roster. In his second season he became a dependable special-teams player, showing the coaches he could live up to the program's long line of tough, unselfish runners. After years of steady work he finally rose to starting tailback, leading his teammates through a demanding final season and setting a school record for touchdowns in a single game. That performance made him a sought-after choice among professional scouts, and it marked the start of a long career filled with highs and lows. He navigated nine seasons in the league and has built a life of service since.</p>
    <p><b><i>In WALKING PAST MIDNIGHT,</i></b> part memoir and part motivation, Moreaux offers a framework for becoming an effective and generous teammate, from setting a game plan to carrying the whole group forward.</p>
    <p><b><i>DELLAN V. MOREAUX</i></b> was the starting fullback for the Ridgeline Stallions and played nine seasons as a pro. He speaks to schools, companies and charities, and lives in the mountains with his wife and their two sons.</p>
    <p><b>Visit www.dellanvmoreaux.com for more.</b></p>
    <div class="flap-sign">
      <div class="brand"><span class="brand-dot"></span>Dellan V. Moreaux</div>
      <div class="flap-url">www.dellanvmoreaux.com</div>
    </div>
  </section>

  <section class="panel panel--back">
    <div class="back-photo" role="img" aria-label="Photo of two football linemen in red uniforms set at the line of scrimmage"></div>
    <h2 class="back-heading">FROM DELLAN V.<br>MOREAUX'S INTRODUCTION</h2>
    <p class="back-body">Becoming a team player is absolutely crucial to your ultimate success. Learning to play within the framework of a team atmosphere not only strengthens your individual ability, but it also gives you a tremendous feeling of accomplishment knowing that you've been instrumental in moving an entire group of people a little closer to the collective dream. I believe that the personal and professional experiences shared in this book will offer strategies that can be used in any team situation, of whether it's a corporate sales force, a little league sports team, a social organization or a family unit.</p>
    <div class="back-brand">
      <div class="brand"><span class="brand-dot"></span>Dellan V. Moreaux</div>
      <div class="back-url">www.dellanvmoreaux.com</div>
    </div>
    <p class="back-charity">portion of the proceeds from the sale of this book will be donated to charity.</p>
  </section>

  <section class="panel panel--spine">
    <div class="spine-text spine-author">MOREAUX</div>
    <div class="spine-text spine-title">WALKING&nbsp;<em>PAST MIDNIGHT</em></div>
    <div class="spine-text spine-foreword">CORWIN<br>BLAKE</div>
  </section>

  <section class="panel panel--front">
    <span class="title-bar title-bar--stem"></span>
    <span class="title-bar title-bar--foot"></span>
    <h1>
      <span class="title title--lead">WALKING</span>
      <span class="title title--mid">PAST</span>
      <span class="title title--tail">MIDNIGHT</span>
    </h1>
    <p class="subtitle">LESSONS FROM<br>QUIET HARBORS</p>
    <p class="author">Dellan V.<br>Moreaux</p>
    <div class="trophies" role="img" aria-label="Two silver championship trophies on a wooden stand"></div>
    <div class="portrait" role="img" aria-label="Author standing in a blue pinstripe suit, hand in pocket"></div>
  </section>

  <div class="foreword">
    <div class="foreword-label">FOREWORD BY</div>
    <div class="foreword-name">CORWIN BLAKE</div>
  </div>

  <section class="flap flap--front">
    <div class="flap-title">WALKING PAST MIDNIGHT</div>
    <div class="flap-subtitle">Lessons from Quiet Harbors</div>
    <p>As the starting fullback for the Ridgeline Stallions, Moreaux cleared the way for his tailback and earned a reputation as the consummate team player. He played a central role in two championship seasons. Now, in <b><i>WALKING PAST MIDNIGHT,</i></b> he explains what it means to be a team player, how to make the most of your talent, master your doubts and overcome limits. He offers strategies that turn individual effort into shared success, from the boardroom to the youth league field, for anyone with a burning desire to succeed.</p>
    <p>Born and raised on the south side of Harborview, Moreaux decided at seventeen that football would be his life. After playing on a struggling high school squad, he made a choice that became the turning point of his young career. He transferred to a school with a great football tradition, where a demanding coach taught him what it takes to reach the next level.</p>
    <p>Though his name was seen weekly in the city papers, his early career was overlooked by many recruiters. Determined to play at the top level, he turned down other offers and chose to walk on at Lakeport State University instead.</p>
    <p class="flap-note"><i>(Continued on back flap)</i></p>
  </section>
</main>
</body>
</html>
```